Laminated Training Card; highly professional yet engaging, colorful, fits branding

We need an 8 1/2" x 11" piece, printed front and back, to inspire and offer instructions for nonprofit leaders on key coaching skills to use with their staff. Though it's in a professional services setting, this piece communicates a sense of fun and excitement to encourage leaders to try out these skills, and keep the training card close at hand. An infographic style would be ideal.

Target Market(s)

Nonprofit leaders will use the laminated training card in a face to face training class, and then take it back to the office to use to 'train' their staff

Industry/Entity Type

Training

Font styles to use
Serif

Requirements
Must have
• See project brief attached
Nice to have
Should not have

```html
<!DOCTYPE html>
<html lang="en">
<head>
<meta charset="utf-8">
<title>Leadership Training Card</title>
<link href="https://fonts.googleapis.com/css2?family=Ubuntu:wght@500;700&family=Lato:wght@300;400&display=swap" rel="stylesheet">
<style>
:root{
  --bg:#d8d2cc;
  --paper:#ffffff;
  --panel-top:#f1f1f1;
  --panel-bottom:#e3e3e3;
  --band-light:#ea8a6e;
  --band-dark:#de552b;
  --ink:#3d3d3d;
  --brand:#6b5548;
  --sky:#8fd0e6;
  --charcoal:#3a3a3a;
}
*{margin:0;padding:0;box-sizing:border-box}
html,body{width:1200px;height:882px;overflow:hidden}
body{background:var(--bg);font-family:"Lato",Arial,sans-serif;font-weight:300;color:var(--ink);position:relative}
.card{position:absolute;top:104px;width:519px;height:671px;background:var(--paper);display:flex;flex-direction:column;box-shadow:0 4px 14px rgba(0,0,0,.25)}
.card--front{left:54px}
.card--back{left:624px}
.brand-header{height:102px;display:flex;align-items:center;padding-left:16px;gap:12px;background:var(--paper)}
.brand-mark{width:62px;height:62px;border-radius:50%;background:var(--brand);flex:none}
.brand-name{font-family:"Lato",Arial,sans-serif;font-weight:400;color:var(--brand);font-size:30px;line-height:32px}
.brand-name small{display:block;font-size:25px}
.band{height:86px;flex:none;position:relative;background:linear-gradient(90deg,var(--band-light),var(--band-dark));display:flex;align-items:center}
.band h2{font-family:"Ubuntu",Arial,sans-serif;font-weight:700;color:#fff;font-size:32px;letter-spacing:.2px;position:absolute;white-space:nowrap}
.band h2.band__title--small{font-size:26px}
.illus{position:absolute;border-radius:10px;background:linear-gradient(135deg,var(--sky),#6fb9d3)}
.illus--dark{background:linear-gradient(135deg,#8fd0e6 0%,#8fd0e6 30%,var(--charcoal) 31%,var(--charcoal) 70%,#8fd0e6 71%)}
.panel{flex:none;background:linear-gradient(180deg,var(--panel-top),var(--panel-bottom));padding:9px 16px 0 16px;font-size:10.4px;line-height:12.8px}
.panel p{margin:0}
.sources{flex:1;background:var(--paper);border-top:2px dotted var(--ink);margin-top:3px;position:relative;padding:18px 0 0 17px}
.sources h3{font-family:"Ubuntu",Arial,sans-serif;font-weight:700;font-size:17px;color:var(--ink);margin-bottom:7px}
.sources__list{font-size:7.6px;line-height:10px;font-weight:400;width:250px}
.sources__mark{position:absolute;left:262px;top:20px;width:62px;height:62px;border-radius:50%;background:var(--brand)}
.contact{position:absolute;left:338px;top:18px;font-size:7.6px;line-height:10.3px;font-weight:400;font-style:normal}
</style>
</head>
<body>

<section class="card card--front">
  <header class="brand-header">
    <div class="brand-mark"></div>
    <div class="brand-name">Northstar Center<small>for Nonprofit Leadership</small></div>
  </header>

  <div class="band">
    <div class="illus" style="left:24px;top:5px;width:112px;height:78px" role="img" aria-label="Flexing figure with a question mark for a head"></div>
    <h2 style="left:164px">Powerful Questions</h2>
  </div>
  <div class="panel" style="height:103px">
    <p>Coach yourself asking powerful questions; they break your internal monologue. Ask others a powerful question — that you don't answer. They will feel deeply heard.</p>
    <p>Dream one moment: What's possible? And establish accountability the next: What should I do when you miss your deadline?</p>
    <p>&nbsp;Asking questions isn't reserved for the leader. Whoever asks the powerful questions is the leader in the moment.</p>
    <p>With whom is it safe to ask powerful questions in your culture?</p>
  </div>

  <div class="band">
    <h2 class="band__title--small" style="left:29px">4 Dimensions of Leadership</h2>
    <div class="illus illus--dark" style="left:379px;top:7px;width:88px;height:79px;border-radius:10px 10px 0 0" role="img" aria-label="Leader figure in a suit with two team members behind"></div>
  </div>
  <div class="panel" style="height:88px">
    <p>Knowing when to move between these stances = leadership mastery.</p>
    <p>Leading from the front: eyes on the vision and staying connected to those who follow</p>
    <p>Leading from the side: &nbsp;locking arms in the company of equals. Eyes on the shared vision, but each has their own path to get there.</p>
    <p>Leading from behind: 'fading' while still holding the space. You've got their backs.</p>
    <p>Leading from above: seeing the big picture</p>
  </div>

  <div class="band">
    <div class="illus" style="left:36px;top:6px;width:120px;height:75px" role="img" aria-label="Three medicine bottles with cross symbols"></div>
    <h2 style="left:210px">4 Team Toxins</h2>
  </div>
  <div class="panel" style="flex:1">
    <p>Defensiveness, blaming, stonewalling and contempt. We all do it, especially when stress is high. There's camaraderie through complaining. &nbsp;But left un-checked, great work comes to a halt.</p>
    <p>Antidotes:</p>
    <p>- &nbsp;Ask: what are you defending? What am I protecting? How can we keep this from spreading?</p>
    <p>- &nbsp;Toxins can flood us. Take a break and come back to the conversation.</p>
    <p>- &nbsp;Check assumptions. 'I assume you have money in your budget. I assume you don't want to be involved. I assume you're supporting me on this.</p>
  </div>
</section>

<section class="card card--back">
  <div class="band">
    <h2 style="left:75px">Brag Bites</h2>
    <div class="illus illus--dark" style="left:340px;top:8px;width:145px;height:75px" role="img" aria-label="Leader figure cheering among a row of team members"></div>
  </div>
  <div class="panel" style="height:96px">
    <p>Brag on the team. Stay away from generalizations; 'I have a great team'. &nbsp;Instead name a value you honored, an obstacle overcome, or what others count on. Have 10 team brag bites in your brag bag ready at all times.</p>
    <p>'We fell short of the goal. But we never gave up.'</p>
    <p>'We didn't expect the new people to step up so quickly. We set aside egos and followed whoever had the best idea.'</p>
    <p>'The whole organization counted on our team's optimism and hopefulness.'</p>
  </div>

  <div class="band">
    <div class="illus" style="left:52px;top:7px;width:90px;height:72px" role="img" aria-label="Rolled paper scroll"></div>
    <h2 style="left:238px">Team Charter</h2>
  </div>
  <div class="panel" style="height:87px">
    <p>Teams don't find their focus from the mission statement. It's too broad, vague and doesn't answer the question: What is our team's unique contribution to achieving the mission? Your &nbsp;answer is your Team Charter. Name your values, what's your impact, how you celebrate success, even what you do when things go wrong.</p>
    <p>The Charters answers the questions: if we weren't here, what would be miss-ing? What do we want people to count on from us?</p>
  </div>

  <div class="band">
    <h2 style="left:45px">Mindfulness</h2>
    <div class="illus illus--dark" style="left:338px;top:2px;width:122px;height:84px;border-radius:40px 40px 0 10px" role="img" aria-label="Head profile with gears inside"></div>
  </div>
  <div class="panel" style="height:112px">
    <p>Whatever gets your attention gets YOU. Become the director of your attention. Mindfulness strength-ens your attention muscles.</p>
    <p>ACCOUNTABILITY CULTURES DELIVER RESULTS</p>
    <p>Improve productivity</p>
    <p>Speed decision making</p>
    <p>Reduce stress and compassion fatigue</p>
    <p>Have more fun and fulfillment</p>
    <p>Build trust</p>
  </div>

  <footer class="sources">
    <h3>SOURCES</h3>
    <div class="sources__list">
      <p>'Speaking Up for the Work You Love' by Dana Whitfield</p>
      <p>Rising Together by (need to fill this in)</p>
      <p>Coaching Practice Academy (CPA): 4-Dimensional Leadership Model</p>
      <p>Levels of Focus: Marcus Ellery &amp; CPA</p>
    </div>
    <div class="sources__mark"></div>
    <address class="contact">
      48 Maple Row, Suite 210<br>
      Riverton, ST 00000<br>
      555-014-2290<br>
      www.northstarcenter.org<br>
      555-014-2290<br>
      hello@northstarcenter.org<br>
      501(c)(3) organization funded by donations
    </address>
  </footer>
</section>

</body>
</html>
```